KVD Insurance - Letterhead

We need a corporate letterhead template (word) and slide show template (PowerPoint) designed for our Insurance Business.
KVD Insurance is in the insurance industry. Please visit our website www.kvdinsurance-example.com
Both templates (word and PowerPoint) must include the KVD logo (attached to this project) and can be very similar in design.
We are after something creative yet professional in design.
Please feel free to ask any questions.

```html
<!DOCTYPE html>
<html lang="en">
<head>
<meta charset="utf-8">
<title>KVD Insurance – Letterhead and Slide Templates</title>
<link rel="stylesheet" href="https://fonts.googleapis.com/css2?family=Montserrat:wght@500&display=swap">
<style>
  :root {
    --backdrop: #e9ecf0;
    --paper: #ffffff;
    --band: #0a0c0b;
    --ink: #111111;
    --accent-orange: #ef5a24;
    --shadow: rgba(20, 30, 50, 0.18);
  }
  * { box-sizing: border-box; margin: 0; padding: 0; }
  html, body {
    width: 1200px;
    height: 640px;
    overflow: hidden;
    background: var(--backdrop);
    font-family: "Montserrat", Arial, sans-serif;
    color: var(--ink);
  }
  .canvas {
    position: relative;
    width: 1200px;
    height: 640px;
  }
  .letterhead, .slide {
    position: absolute;
    background: var(--paper);
    box-shadow: 0 4px 14px var(--shadow);
    overflow: hidden;
  }
  .letterhead {
    left: 90px;
    top: 40px;
    width: 416px;
    height: 560px;
  }
  .slide {
    left: 570px;
    top: 126px;
    width: 560px;
    height: 388px;
  }
  .side-band {
    position: absolute;
    left: 0;
    top: 0;
    bottom: 0;
    background: var(--band);
  }
  .letterhead .side-band { width: 70px; }
  .slide .side-band { width: 72px; }
  .band-dot {
    position: absolute;
    border-radius: 50%;
    background: var(--accent-orange);
  }
  .letterhead .band-dot { width: 30px; height: 30px; left: 20px; bottom: 26px; }
  .slide .band-dot { width: 30px; height: 30px; left: 21px; bottom: 28px; }
  .brand-name {
    position: absolute;
    font-weight: 500;
    text-transform: uppercase;
    letter-spacing: 0.06em;
    line-height: 1;
    color: var(--ink);
    white-space: nowrap;
  }
  .letterhead .brand-name { right: 28px; top: 46px; font-size: 15px; }
  .slide .brand-name { right: 32px; top: 46px; font-size: 15px; }
  .contact {
    position: absolute;
    left: 82px;
    bottom: 18px;
    font-size: 6px;
    font-style: normal;
    font-weight: 500;
    line-height: 1.35;
    color: var(--ink);
    white-space: nowrap;
  }
  .contact-phone {
    display: flex;
    align-items: center;
    gap: 3px;
  }
  .contact-phone svg { width: 6px; height: 6px; }
</style>
</head>
<body>
  <main class="canvas">
    <section class="letterhead" aria-label="KVD Insurance letterhead">
      <div class="side-band">
        <span class="band-dot"></span>
      </div>
      <p class="brand-name">KVD Insurance</p>
      <address class="contact">
        <span class="contact-phone">
          <svg viewBox="0 0 10 10" aria-hidden="true"><path d="M2 1h2l1 2-1.2 1a5 5 0 0 0 2.2 2.2L7 5l2 1v2a1 1 0 0 1-1 1A8 8 0 0 1 1 2a1 1 0 0 1 1-1z" fill="#111"/></svg>
          00 4150 67812
        </span>
        Harbour Lane, 4/210 Mill road, RVN PO BOX 5678
      </address>
    </section>

    <section class="slide" aria-label="KVD Insurance slide template">
      <div class="side-band">
        <span class="band-dot"></span>
      </div>
      <p class="brand-name">KVD Insurance</p>
    </section>
  </main>
</body>
</html>
```